K&T Fixit and Rebuild general contracting business card design

I already have a logo that I want to use and I need a card that uses that logo and color scheme on the front with the address phone numbers and email and on the back a place for technicians to write in their name and phone number when they hand it out. It will need the License number of License #KTFXTRB318QN.
It should say General Contractor under the company name. The address is
4417 NE 3rd Ave, Ste D246
Vancouver, WA 98612
www.kandtfixitandrebuild.example
office@kandtfixitandrebuild.example
360-555-0182 is the telephone number
360-555-0149 is the fax number

Target Market(s)

Homeowners needing remodel work or repairs in their home.

Industry/Entity Type

Construction

Contact Information for Business Card

Business name, address, phone number, license number, fax number, email, and website on the front and a place to fill in technician's name and number

Font styles to use
Serif

Requirements
Must have
• Business name, address, phone number, license number, fax number, email, and website on the front and a place to fill in technician's name and number
Nice to have
• I uploaded an example of a front that is good.
Should not have
• Froo froo or extra embellishments.

```html
<!DOCTYPE html>
<html lang="en">
<head>
<meta charset="utf-8">
<title>K&amp;T Fixit and Rebuild – Business Card</title>
<link rel="stylesheet" href="https://fonts.googleapis.com/css2?family=Roboto:wght@400;500;700&display=swap">
<style>
  :root {
    --copper: #b4673f;
    --ink: #4a4a4a;
    --paper: #ffffff;
    --backdrop: #b3b3b3;
    --card-dark: #1b1d1c;
    --dark-mark: #3a3c3b;
    --dark-line: #4a4c4b;
    --dark-label: #8a8c8b;
  }
  * { margin: 0; padding: 0; box-sizing: border-box; }
  html, body { width: 1200px; height: 1080px; overflow: hidden; }
  body {
    background: var(--backdrop);
    font-family: "Roboto", Arial, sans-serif;
    position: relative;
  }
  .card {
    position: absolute;
    left: 275px;
    width: 650px;
    height: 371px;
    overflow: hidden;
  }
  .card-front { top: 134px; background: var(--paper); }
  .card-back { top: 574px; background: var(--card-dark); }

  .brand-block {
    position: absolute;
    left: 340px;
    top: 42px;
    width: 260px;
    text-align: center;
  }
  .brand {
    color: var(--copper);
    font-weight: 700;
    font-size: 36px;
    line-height: 1.08;
  }
  .brand-tagline {
    margin-top: 10px;
    font-size: 15px;
    font-weight: 500;
    letter-spacing: 2.5px;
    text-transform: uppercase;
    color: var(--ink);
  }

  .name-accent {
    position: absolute;
    left: 0; top: 194px;
    width: 10px; height: 41px;
    background: var(--copper);
  }
  .person-name {
    position: absolute;
    left: 43px; top: 190px;
    font-size: 20px; font-weight: 700;
    color: var(--copper);
    letter-spacing: 0.2px;
  }
  .person-title {
    position: absolute;
    left: 43px; top: 217px;
    font-size: 15px;
    color: var(--ink);
  }
  .divider {
    position: absolute;
    left: 44px; top: 242px;
    width: 557px; height: 1px;
    background: var(--copper);
  }
  .contact-list {
    position: absolute;
    left: 43px; top: 254px;
    list-style: none;
    font-size: 15px;
    color: var(--ink);
  }
  .contact-list li {
    display: flex; align-items: center;
    height: 19.5px;
  }
  .contact-list svg { width: 11px; height: 11px; margin-right: 6px; fill: var(--copper); flex: none; }
  .address {
    position: absolute;
    right: 49px; top: 290px;
    text-align: right;
    font-size: 15px;
    line-height: 22px;
    color: var(--ink);
  }
  .footer-band { position: absolute; left: 0; top: 346px; width: 650px; height: 25px; }
  .license {
    position: absolute;
    right: 45px; top: 350px;
    font-size: 15px;
    color: var(--paper);
  }

  .back-brand-block {
    position: absolute;
    left: 0; right: 0; top: 78px;
    text-align: center;
  }
  .back-brand {
    color: var(--dark-mark);
    font-weight: 700;
    font-size: 40px;
    line-height: 1.1;
  }
  .back-tagline {
    margin-top: 8px;
    font-size: 14px;
    font-weight: 500;
    letter-spacing: 2.5px;
    text-transform: uppercase;
    color: var(--dark-mark);
  }
  .tech-fields {
    position: absolute;
    left: 150px; right: 150px; top: 262px;
  }
  .tech-field {
    display: flex;
    align-items: flex-end;
    height: 34px;
    font-size: 13px;
    color: var(--dark-label);
  }
  .tech-field .label { width: 92px; flex: none; padding-bottom: 3px; }
  .tech-field .write-line { flex: 1; border-bottom: 1px solid var(--dark-line); height: 1px; }
</style>
</head>
<body>
  <section class="card card-front">
    <div class="brand-block">
      <div class="brand">K&amp;T Fixit and<br>Rebuild</div>
      <div class="brand-tagline">General Contractor</div>
    </div>

    <span class="name-accent"></span>
    <div class="person-name">DANIEL WHITCOMBE</div>
    <div class="person-title">Founder &amp; CEO</div>
    <div class="divider"></div>

    <ul class="contact-list">
      <li><svg viewBox="0 0 24 24"><path d="M6.6 10.8a15.1 15.1 0 0 0 6.6 6.6l2.2-2.2c.3-.3.7-.4 1-.2 1.1.4 2.3.6 3.6.6.6 0 1 .4 1 1V20c0 .6-.4 1-1 1A17 17 0 0 1 3 4c0-.6.4-1 1-1h3.5c.6 0 1 .4 1 1 0 1.3.2 2.5.6 3.6.1.3 0 .7-.2 1z"/></svg>360-555-0182</li>
      <li><svg viewBox="0 0 24 24"><path d="M6 2h12v6H6zM3 9h18a1 1 0 0 1 1 1v7h-4v5H6v-5H2v-7a1 1 0 0 1 1-1zm5 7v4h8v-4z"/></svg>360-555-0149</li>
      <li><svg viewBox="0 0 24 24"><path d="M2 5h20v14H2zm2 2v.5l8 5 8-5V7l-8 5z"/></svg>office@kandtfixitandrebuild.example</li>
      <li><svg viewBox="0 0 24 24"><path d="M12 2a10 10 0 1 0 0 20 10 10 0 0 0 0-20zm0 2c.9 1 1.7 2.7 2 5h-4c.3-2.3 1.1-4 2-5zM4.3 11h3.7c0 .7 0 1.3.1 2H4.3a8 8 0 0 1 0-2zm5.7 0h4a17 17 0 0 1 0 2h-4a17 17 0 0 1 0-2zm6 0h3.7a8 8 0 0 1 0 2H16c.1-.7.1-1.3 0-2zm-6 4h4c-.3 2.3-1.1 4-2 5-.9-1-1.7-2.7-2-5z"/></svg>www.kandtfixitandrebuild.example</li>
    </ul>

    <div class="address">4417 NE 3rd Ave, Ste D246<br>Vancouver, WA 98612</div>

    <svg class="footer-band" viewBox="0 0 650 25" preserveAspectRatio="none" aria-hidden="true">
      <rect x="0" y="13" width="392" height="12" fill="#b4673f"/>
      <polygon points="383,25 395,15 399,15 387,25" fill="#b4673f"/>
      <polygon points="402,25 426,0 650,0 650,25" fill="#b4673f"/>
    </svg>
    <div class="license">License #KTFXTRB318QN.</div>
  </section>

  <section class="card card-back">
    <div class="back-brand-block">
      <div class="back-brand">K&amp;T Fixit<br>and Rebuild</div>
      <div class="back-tagline">General Contractor</div>
    </div>
    <div class="tech-fields">
      <div class="tech-field"><span class="label">Technician</span><span class="write-line"></span></div>
      <div class="tech-field"><span class="label">Phone</span><span class="write-line"></span></div>
    </div>
  </section>
</body>
</html>
```